Industrial Professional Business Card Design (Vantrel Systems)

Would like professional looking business cards. Not too busy leaning towards minimal. Should have a slogan like:
"Industrial Automation and Control".

We are a tech company that programs industrial PLC computers. We also develop custom hardware solutions. Please use the logo for inspiration.

Target Market(s)

Mining, industrial, processing, automation, factory

Industry/Entity Type

Engineering

Contact Information for Business Card

Name, phone, email, website. job title.

Font styles to use
Other font styles liked:
• droid sans

Requirements
Must have
• Use colours that go well with the logo. Not too busy design.

```html
<!DOCTYPE html>
<html lang="en">
<head>
<meta charset="utf-8">
<title>Vantrel Systems — Business Card</title>
<link rel="stylesheet" href="https://fonts.googleapis.com/css2?family=Noto+Sans:wght@400;700&family=Poppins:wght@400;500&display=swap">
<style>
  :root {
    --backdrop: #9a9a9a;
    --navy: #1b3a62;
    --navy-deep: #163154;
    --orange: #f26b21;
    --white: #ffffff;
    --ink: #4a4f57;
    --faint-blue: #e6ebf1;
    --faint-orange: #fbe3d8;
  }
  * { box-sizing: border-box; margin: 0; padding: 0; }
  html, body { width: 1200px; height: 900px; overflow: hidden; }
  body {
    background: var(--backdrop);
    font-family: "Noto Sans", sans-serif;
    position: relative;
  }
  .card {
    position: absolute;
    width: 520px;
    height: 300px;
    border-radius: 22px;
    overflow: hidden;
  }
  .card-back {
    left: 110px; top: 120px;
    background: var(--navy);
    color: var(--white);
    display: flex; flex-direction: column; align-items: center; justify-content: center;
  }
  .brand {
    display: flex; align-items: center; gap: 12px;
    font-family: "Noto Sans", sans-serif;
    font-weight: 400;
    font-size: 34px;
    letter-spacing: 0.5px;
  }
  .brand-dot { width: 30px; height: 30px; border-radius: 50%; background: currentColor; }
  .card-back .tagline {
    margin-top: 40px;
    font-family: "Poppins", sans-serif;
    font-size: 12px;
    letter-spacing: 0.6px;
  }
  .card-front {
    left: 570px; top: 480px;
    background: var(--white);
  }
  .watermark {
    position: absolute; right: -60px; top: -70px;
    width: 330px; height: 330px; border-radius: 50%;
    background: var(--faint-blue);
    border: 26px solid var(--faint-orange);
  }
  .card-front .brand {
    position: absolute; left: 40px; top: 42px;
    color: var(--navy);
    font-size: 28px;
  }
  .card-front .brand-dot { width: 24px; height: 24px; background: var(--orange); }
  .person { position: absolute; left: 40px; top: 132px; }
  .person-name { font-weight: 700; font-size: 20px; color: var(--navy); }
  .person-title { font-size: 14px; color: var(--orange); margin-top: 2px; }
  .contacts { position: absolute; left: 40px; top: 200px; list-style: none; }
  .contacts li {
    display: flex; align-items: center; gap: 10px;
    font-size: 13px; color: var(--ink); line-height: 22px;
  }
  .contacts svg { width: 12px; height: 12px; fill: var(--navy); }
</style>
</head>
<body>
  <section class="card card-back">
    <div class="brand"><span class="brand-dot"></span>Vantrel Systems</div>
    <p class="tagline">Industrial Automation &amp; Control</p>
  </section>

  <section class="card card-front">
    <div class="watermark" role="img" aria-label="Large faint brand decoration"></div>
    <div class="brand"><span class="brand-dot"></span>Vantrel Systems</div>
    <div class="person">
      <p class="person-name">Daniel Hargrove</p>
      <p class="person-title">President</p>
    </div>
    <ul class="contacts">
      <li>
        <svg viewBox="0 0 24 24" aria-hidden="true"><path d="M6.6 10.8a15 15 0 0 0 6.6 6.6l2.2-2.2c.3-.3.7-.4 1-.2 1.1.4 2.3.6 3.6.6.6 0 1 .4 1 1V20c0 .6-.4 1-1 1C10.6 21 3 13.4 3 4c0-.6.4-1 1-1h3.5c.6 0 1 .4 1 1 0 1.3.2 2.5.6 3.6.1.3 0 .7-.2 1z"/></svg>
        555-214-3076
      </li>
      <li>
        <svg viewBox="0 0 24 24" aria-hidden="true"><path d="M2 5h20v14H2z M2 5l10 8 10-8" /></svg>
        info@vantrelsystems.com
      </li>
      <li>
        <svg viewBox="0 0 24 24" aria-hidden="true"><circle cx="12" cy="12" r="10"/></svg>
        www.vantrelsystems.com
      </li>
    </ul>
  </section>
</body>
</html>
```